Brochure design for a cyber security tradeshow

We are looking to design a brochure of A4 size, suitable for printing on both sides.
For conference on information security.
We will provide full content (in English) and the overall design style we want.
We are interested in combining Infographic inside the brochure.

Attached:
- Word file with the content. the infographic insdie is just an example. Please take the content, and be creative:)

For style guidelines:
- Take a look on our website: www.brivoka.com
- Take a look on this specific video: https://www.vidstreamo.com/watch?v=QTR4mPzLwdf
We want the design will be based on this style.

Target Market(s)

Cyber Security managers

Industry/Entity Type

Printing

Font styles to use
Sans Serif

Colors
f37122
0392cd
000000
ffffff
86cfc6
fece3e

Requirements
Must have
• Cool infographic, and the company logo

```html
<!DOCTYPE html>
<html lang="en">
<head>
<meta charset="UTF-8">
<title>flowGuard – 10 Ways to Minimize Damage from Cyber-Attacks</title>
<link rel="stylesheet" href="https://fonts.googleapis.com/css2?family=Open+Sans:wght@400;600&display=swap">
<style>
  :root {
    --page-bg: #e8bd68;
    --frame: #3a3226;
    --accent: #f37122;
    --text-light: #ffffff;
    --band: #ffffff;
    --partner-ink: #3b3b3b;
    --partner-dot: #0392cd;
  }
  * { margin: 0; padding: 0; box-sizing: border-box; }
  html, body { width: 800px; height: 1200px; overflow: hidden; }
  body {
    font-family: "Open Sans", Arial, sans-serif;
    background: var(--page-bg);
  }
  .page {
    position: relative;
    width: 800px;
    height: 1200px;
    background: var(--page-bg);
    border: 1.5px solid var(--frame);
  }
  .integrations-title {
    position: absolute;
    left: 59px;
    top: 55px;
    font-size: 22.5px;
    font-weight: 600;
    color: var(--accent);
  }
  .partner-band {
    position: absolute;
    left: 48px;
    top: 121px;
    width: 703px;
    height: 58px;
    background: var(--band);
    list-style: none;
  }
  .partner {
    position: absolute;
    top: 50%;
    transform: translate(-50%, -50%);
    display: flex;
    align-items: center;
    gap: 4px;
    font-size: 10px;
    font-weight: 600;
    color: var(--partner-ink);
    white-space: nowrap;
  }
  .partner-dot {
    width: 7px; height: 7px;
    border-radius: 50%;
    background: var(--partner-dot);
  }
  .ways-heading {
    position: absolute;
    left: 48px;
    top: 228px;
    width: 720px;
    font-size: 21px;
    line-height: 27px;
    font-weight: 400;
    color: var(--accent);
    text-transform: uppercase;
  }
  .ways-list {
    position: absolute;
    left: 48px;
    top: 324px;
    width: 700px;
    list-style: none;
    color: var(--text-light);
    font-size: 19.4px;
    line-height: 24px;
    text-shadow: 0 0 1px rgba(120, 80, 20, 0.35);
  }
  .way {
    position: relative;
    padding-left: 25px;
    margin-bottom: 24px;
  }
  .way-number {
    position: absolute;
    left: 0;
    top: 0;
  }
  .way-number.wide { position: static; padding-right: 20px; margin-left: -25px; }
</style>
</head>
<body>
<main class="page">
  <h2 class="integrations-title">flowGuard integrations include:</h2>

  <ul class="partner-band">
    <li class="partner" style="left:84px"><span class="partner-dot"></span>Arcvane</li>
    <li class="partner" style="left:218px"><span class="partner-dot"></span>Corelia</li>
    <li class="partner" style="left:356px"><span class="partner-dot"></span>Ravix</li>
    <li class="partner" style="left:490px"><span class="partner-dot"></span>Spindle</li>
    <li class="partner" style="left:626px"><span class="partner-dot"></span>Quadrix</li>
  </ul>

  <h1 class="ways-heading">10 ways how flowGuard can help you minimize damage from cyber-attacks:</h1>

  <ol class="ways-list">
    <li class="way"><span class="way-number">1.</span>Respond to SIEM security events and automatically execute specified procedures to extract additional information, manage incident resolution, and communicate with relevant personnel as needed to solve more complex events.</li>
    <li class="way"><span class="way-number">2.</span>Respond to antivirus system alerts by executing policies to prevent intrusions, the spread of viruses, and other dangerous external threats.</li>
    <li class="way"><span class="way-number">3.</span>Remotely disconnect and lock any unauthorized or suspicious devices and/ or computers from the network instantly via email or SMS.</li>
    <li class="way"><span class="way-number">4.</span>Conduct remote, on-demand checks of users who are currently logged in to a certain workstation, using either email or SMS.</li>
    <li class="way"><span class="way-number">5.</span>Generate daily reports of users that have logged in to the domain during off hour timeframes.</li>
    <li class="way"><span class="way-number">6.</span>Enable/disable user logins within certain time frames to maintain better control over remote user connections.</li>
    <li class="way"><span class="way-number">7.</span>Scan and block computers and services identified as known-bad (based on known activities).</li>
    <li class="way"><span class="way-number">8.</span>Perform deep investigation of suspicious computers by automatically installing forensic tools.</li>
    <li class="way"><span class="way-number">9.</span>Block DoS attacks by dynamically adapting security and communications to external resources.</li>
    <li class="way"><span class="way-number wide">10.</span>Auto-recover from defacement. by automatically restoring a backup of your website configuration and files.</li>
  </ol>
</main>
</body>
</html>
```